a4 size poster for theatre school

I am looking for an eye catching poster for my theatre school - Bright Lantern Stage school - View our website here for the style we have already www.brightlanternstage.co.uk

Wording needs to include;

* Award Winning, Accredited, Affordable Performing Arts Classes taught by Leading Industry Experts

* Ages 4- 21 years

* All classes contain all three disciplines of Drama, Singing & Dance keeping cost low and enjoyment high

* Classes offered;
Drama
PQVR
Singing
KSBU dance
Freestyle Ballet
Freestyle Tap
Contemporary
Street
Jazz Musical Theatre

* FREE casting agency for TV and Theatre Available. Ten pupils currently performing in West End Productions, 8 pupils currently on screen in TV commercials, several pupils currently working on film & TV projects for Zorbiville, Quellmark Plus & Vista 9.

* Optional KSBU and PQVR exams

* Unparalleled performance opportunities both locally and in the West End

Our quality training is evident in our pupils success

* Now in our successful 17th Year!

* Awarded recognition from the Board for Stagecraft, Voice and Movement Studies - The industry regulator for children's performing arts training.

Target Market(s)

Parents & Children ages 4-21 years

Industry/Entity Type

Performing arts

Font styles to use
Other font styles liked:
• Arvo

Colors
EB3D1F
EC4F4E
F09395
F8D3D4
FCEDEE
6B429C
8869AF
B7A5CE
E3DAEB
F3F0F8

Requirements
Must have
• A good mix of photo's pf boys & girls. Different ethnicities. Different ages
Nice to have
• Wording very clear
Should not have
• Too many words

```html
<!DOCTYPE html>
<html lang="en">
<head>
<meta charset="utf-8">
<title>Bright Lantern Stage school poster</title>
<link href="https://fonts.googleapis.com/css2?family=Oswald:wght@500;600;700&family=Ubuntu:wght@300;400;500;700&display=swap" rel="stylesheet">
<style>
  :root {
    --ink: #000000;
    --paper: #ffffff;
    --yellow: #ffe019;
    --red: #e8202e;
    --red-text: #ff2a35;
    --pink-frame: #f09395;
    --stage-top: #0d1626;
    --stage-mid: #2a1f46;
    --stage-low: #4a1f3a;
    --badge-fill: #ffffff;
    --backdrop: #2b2d31;
  }
  * { box-sizing: border-box; margin: 0; padding: 0; }
  html, body { width: 1200px; height: 1200px; overflow: hidden; background: var(--backdrop); }
  .poster {
    position: absolute; left: 176px; top: 0;
    width: 902px; height: 1278px;
    transform: scale(0.939); transform-origin: top left;
    background: var(--ink); color: var(--paper);
    font-family: "Ubuntu", sans-serif; overflow: hidden;
  }
  .hero-photo {
    position: absolute; left: 0; top: 0; width: 902px; height: 640px;
    background: radial-gradient(ellipse at 55% 45%, #5a4a7a 0%, var(--stage-mid) 40%, var(--stage-top) 75%),
                linear-gradient(180deg, var(--stage-top), var(--stage-low));
  }
  .snapshot {
    position: absolute; width: 118px; height: 92px;
    border: 7px solid var(--pink-frame);
    background: linear-gradient(135deg, #8a5a3a, #3c2a50);
  }
  .snap-1 { left: 100px; top: 362px; transform: rotate(14deg); }
  .snap-2 { left: 20px; top: 425px; transform: rotate(-12deg); background: linear-gradient(135deg,#b07a2a,#5a3020); }
  .snap-3 { left: 28px; top: 518px; transform: rotate(10deg); background: linear-gradient(135deg,#6a3a1a,#d08a3a); }
  .snap-4 { left: 686px; top: 358px; transform: rotate(-14deg); background: linear-gradient(135deg,#a04a2a,#2a2a60); }
  .snap-5 { left: 756px; top: 430px; transform: rotate(14deg); background: linear-gradient(135deg,#2a3a9a,#7a2a6a); }
  .snap-6 { left: 742px; top: 522px; transform: rotate(-13deg); background: linear-gradient(135deg,#c0a070,#6a4a2a); }

  .brand {
    position: absolute; left: 52px; top: 48px; width: 240px;
    display: flex; align-items: center; gap: 12px;
  }
  .brand-dot { flex: 0 0 40px; height: 40px; border-radius: 50%; background: var(--yellow); }
  .brand-name {
    font-family: "Oswald", sans-serif; font-weight: 600; font-size: 30px; line-height: 1.1;
    color: var(--yellow); text-transform: uppercase;
  }
  .headline {
    position: absolute; right: 53px; top: 40px; text-align: right;
    font-family: "Oswald", sans-serif; font-weight: 600; font-size: 27px; line-height: 33px;
  }
  .headline .accent { color: var(--yellow); }
  .ages {
    position: absolute; right: 53px; top: 114px;
    font-family: "Oswald", sans-serif; font-weight: 600; font-style: italic; font-size: 30px;
    color: var(--yellow);
  }
  .ages .age-range { color: var(--red-text); }

  .disciplines-band {
    position: absolute; left: 0; top: 630px; width: 902px; height: 95px;
    background: var(--red); text-align: center;
    font-family: "Oswald", sans-serif; font-weight: 600; font-size: 30px; line-height: 37px;
    padding-top: 11px;
  }
  .disciplines-band .lead { color: var(--yellow); text-transform: uppercase; }

  .classes-box {
    position: absolute; left: 52px; top: 768px; width: 372px; height: 219px;
    border: 2px solid var(--yellow); border-radius: 8px;
  }
  .classes-label {
    position: absolute; left: 52px; top: 753px; height: 34px; padding: 0 18px 0 10px;
    background: var(--yellow); color: var(--ink); border-radius: 0 17px 17px 0;
    font-family: "Ubuntu", sans-serif; font-weight: 700; font-size: 24px; line-height: 34px;
    text-transform: uppercase;
  }
  .class-list { position: absolute; list-style: none; font-size: 17px; }
  .class-list li { display: flex; align-items: center; height: 36.5px; gap: 10px; }
  .class-list svg { width: 21px; height: 21px; flex: none; }
  .col-a { left: 62px; top: 794px; }
  .col-b { left: 205px; top: 794px; }

  .point {
    position: absolute; display: flex; gap: 10px; font-size: 17px; line-height: 22px; text-align: justify;
  }
  .point svg { width: 22px; height: 14px; flex: none; margin-top: 5px; }
  .point-exams { left: 62px; top: 1014px; width: 370px; }
  .point-stages { left: 62px; top: 1062px; width: 370px; }
  .point-casting { left: 478px; top: 758px; width: 372px; }
  .point-casting .title { color: var(--yellow); font-weight: 700; font-size: 16.5px; }
  .point-casting .body { font-size: 16.5px; line-height: 22px; margin-top: 4px; text-align: justify; }

  .phone {
    position: absolute; left: 50px; top: 1138px;
    font-family: "Oswald", sans-serif; font-weight: 700; font-size: 64px; line-height: 70px;
    letter-spacing: -0.5px;
  }
  .website {
    position: absolute; left: 52px; top: 1210px;
    font-weight: 300; font-size: 28px; color: var(--red-text); letter-spacing: 0.5px;
  }

  .quality {
    position: absolute; left: 478px; top: 942px; width: 372px;
    color: var(--yellow); font-weight: 700; font-size: 19px; line-height: 26px; text-align: justify;
  }
  .anniversary {
    position: absolute; left: 478px; top: 1006px;
    font-weight: 500; font-size: 23.5px; color: var(--red-text);
  }
  .anniversary .year { color: var(--yellow); }
  .recognition {
    position: absolute; left: 478px; top: 1045px; width: 372px;
    font-size: 14.5px; line-height: 20px; text-align: justify;
  }
  .accreditation-badge {
    position: absolute; left: 477px; top: 1130px; width: 370px; height: 108px;
    background: var(--badge-fill);
  }
</style>
</head>
<body>
<main class="poster">
  <div class="hero-photo" role="img" aria-label="Stage photograph of a group of young performers mid dance number under stage lights"></div>
  <div class="snapshot snap-1" role="img" aria-label="Photo of a street dance class"></div>
  <div class="snapshot snap-2" role="img" aria-label="Photo of a musical theatre scene with a car prop"></div>
  <div class="snapshot snap-3" role="img" aria-label="Photo of two pupils in stage costume and make-up"></div>
  <div class="snapshot snap-4" role="img" aria-label="Photo of a contemporary dance lift on stage"></div>
  <div class="snapshot snap-5" role="img" aria-label="Photo of dancers leaping under blue stage light"></div>
  <div class="snapshot snap-6" role="img" aria-label="Photo of young pupils performing in costume"></div>

  <div class="brand">
    <span class="brand-dot"></span>
    <span class="brand-name">Bright Lantern Stage school</span>
  </div>

  <h1 class="headline">
    <span class="accent">Award Winning, Accredited, Affordable Performing</span><br>
    Arts Classes taught by Leading Industry Experts
  </h1>
  <p class="ages">Ages <span class="age-range">4- 21</span> years</p>

  <section class="disciplines-band">
    <div class="lead">All classes contain all three disciplines of</div>
    <div>Drama, Singing &amp; Dance keeping cost low and enjoyment high</div>
  </section>

  <div class="classes-box"></div>
  <h2 class="classes-label">Classes offered</h2>
  <ul class="class-list col-a">
    <li><svg viewBox="0 0 24 24"><path fill="#ffe019" d="M12 1l3.2 7.3 7.8.7-5.9 5.2 1.8 7.8L12 18l-6.9 4 1.8-7.8L1 9l7.8-.7z"/></svg>Drama</li>
    <li><svg viewBox="0 0 24 24"><path fill="#ffe019" d="M12 1l3.2 7.3 7.8.7-5.9 5.2 1.8 7.8L12 18l-6.9 4 1.8-7.8L1 9l7.8-.7z"/></svg>PQVR</li>
    <li><svg viewBox="0 0 24 24"><path fill="#ffe019" d="M12 1l3.2 7.3 7.8.7-5.9 5.2 1.8 7.8L12 18l-6.9 4 1.8-7.8L1 9l7.8-.7z"/></svg>Singing</li>
    <li><svg viewBox="0 0 24 24"><path fill="#ffe019" d="M12 1l3.2 7.3 7.8.7-5.9 5.2 1.8 7.8L12 18l-6.9 4 1.8-7.8L1 9l7.8-.7z"/></svg>Street</li>
    <li><svg viewBox="0 0 24 24"><path fill="#ffe019" d="M12 1l3.2 7.3 7.8.7-5.9 5.2 1.8 7.8L12 18l-6.9 4 1.8-7.8L1 9l7.8-.7z"/></svg>KSBU dance</li>
  </ul>
  <ul class="class-list col-b">
    <li><svg viewBox="0 0 24 24"><path fill="#ffe019" d="M12 1l3.2 7.3 7.8.7-5.9 5.2 1.8 7.8L12 18l-6.9 4 1.8-7.8L1 9l7.8-.7z"/></svg>Freestyle Tap</li>
    <li><svg viewBox="0 0 24 24"><path fill="#ffe019" d="M12 1l3.2 7.3 7.8.7-5.9 5.2 1.8 7.8L12 18l-6.9 4 1.8-7.8L1 9l7.8-.7z"/></svg>Freestyle Ballet</li>
    <li><svg viewBox="0 0 24 24"><path fill="#ffe019" d="M12 1l3.2 7.3 7.8.7-5.9 5.2 1.8 7.8L12 18l-6.9 4 1.8-7.8L1 9l7.8-.7z"/></svg>Contemporary</li>
    <li><svg viewBox="0 0 24 24"><path fill="#ffe019" d="M12 1l3.2 7.3 7.8.7-5.9 5.2 1.8 7.8L12 18l-6.9 4 1.8-7.8L1 9l7.8-.7z"/></svg>Jazz Musical Theatre</li>
  </ul>

  <p class="point point-exams">
    <svg viewBox="0 0 22 14"><path d="M1 1l6 6-6 6" fill="none" stroke="#ffe019" stroke-width="3"/><path d="M9 1l6 6-6 6" fill="none" stroke="#e8202e" stroke-width="3"/></svg>
    <span>Optional KSBU and PQVR exams</span>
  </p>
  <p class="point point-stages">
    <svg viewBox="0 0 22 14"><path d="M1 1l6 6-6 6" fill="none" stroke="#ffe019" stroke-width="3"/><path d="M9 1l6 6-6 6" fill="none" stroke="#e8202e" stroke-width="3"/></svg>
    <span>Unparalleled performance opportunities both locally and in the West End</span>
  </p>

  <p class="phone">020 7946 0182</p>
  <p class="website">www.brightlanternstage.co.uk</p>

  <div class="point point-casting">
    <svg viewBox="0 0 22 14"><path d="M1 1l6 6-6 6" fill="none" stroke="#ffe019" stroke-width="3"/><path d="M9 1l6 6-6 6" fill="none" stroke="#e8202e" stroke-width="3"/></svg>
    <div>
      <p class="title">FREE casting agency for TV and Theatre Available.</p>
      <p class="body">Ten pupils currently performing in West End Productions, 8 pupils currently on screen in TV commercials, several pupils currently working on film &amp; TV projects for Zorbiville, Quellmark Plus &amp; Vista 9.</p>
    </div>
  </div>

  <p class="quality">Our quality training is evident in our pupils success</p>
  <p class="anniversary">Now in our successful <span class="year">17th Year!</span></p>
  <p class="recognition">Awarded recognition from the Board for Stagecraft, Voice and Movement Studies - The industry regulator for children's performing arts training.</p>

  <div class="accreditation-badge" role="img" aria-label="Recognised school accreditation badge"></div>
</main>
</body>
</html>
```